Volbex (Pathways for trade momentum) website

My plan is to offer a marketplace where by businesses (SME and Corporates) are able to post specific requirements, be that debt funding advice or other types of advice (legal/accountant) on the volbex website and advisors can seek to 'pitch' to the client.

clients should be anonymous - maybe a specific client number? (this is reduces the risk of bypass) and have the ability to choose the advisor via the advisors profile.

Advisors could potential use there Peerlane profile to auto complete on Volbex - not sure if this is possible or costs involved, however this would be ideal.

I would think Wordpress would be the best platform for this type of platform, however I would be guided by the experts.

I would need any code written in html 5 to allow for various devices (mobile, tablets, desktop)

Logo design is currently being completed also via Sketch Hive and I'm finalising colours ext now, so could provide advice in due course.

additional requirements (medium to longer term)
longer term I would be looking to add addition aspects to the site including algorithms, specific financial calculations, some of which I would be able to complete myself.

similar websites would be:
https://www.taskmorn.com.au
http://www.fundvale.com.au

Industry/Entity Type

Debt

Coding

Coded - Design and coding required

```html
<!DOCTYPE html>
<html lang="en">
<head>
<meta charset="utf-8">
<title>Volbex – Pathways for trade momentum</title>
<link rel="stylesheet" href="https://fonts.googleapis.com/css2?family=Arimo:wght@400;700&family=Open+Sans:ital,wght@0,400;0,600;0,700;1,400&display=swap">
<style>
:root{
  --brand:#0b5aa6;
  --brand-dark:#08488c;
  --footer:#0a4f99;
  --footer-bar:#0c315c;
  --ink:#333;
  --muted:#555;
  --band:#d6e7f7;
  --line:#7aa7d6;
  --heading:#0f5fa8;
}
*{box-sizing:border-box;margin:0;padding:0}
html,body{width:682px;height:1200px;overflow:hidden;background:#fff}
body{position:relative;font-family:"Arimo",Arial,sans-serif;color:var(--ink)}
.abs{position:absolute}
.topline{left:0;top:0;width:682px;height:4px;background:#222}
.logo{left:100px;top:14px;font-size:22px;font-weight:700;color:#111;border-bottom:2px solid #111;line-height:22px;padding-bottom:1px}
.register{left:360px;top:18px;font-size:9px;color:var(--brand);word-spacing:3px}
.search{left:468px;top:17px;width:113px;height:17px;border:1px solid var(--brand);display:flex}
.search span{flex:1;font-size:7px;color:#999;padding:4px 5px}
.search b{width:22px;background:var(--brand);display:flex;align-items:center;justify-content:center}
.nav{left:0;top:43px;width:682px;height:19px;background:var(--brand);display:flex;justify-content:center;align-items:center;gap:0;font-size:9px;color:#fff}
.nav span{padding:0 5px}
.nav i{font-style:normal;opacity:.8}
.hero{left:0;top:62px;width:682px;height:340px;background:linear-gradient(120deg,#dfe6ee 0%,#9fb8d2 35%,#c9d4e0 55%,#5b6570 75%,#e7ebef 100%)}
.hero-line{left:0;top:402px;width:682px;height:3px;background:var(--brand)}
.welcome{left:100px;top:232px;width:481px;height:110px;background:rgba(24,104,186,.72);color:#fff;text-align:center;padding:5px 14px}
.welcome h1{font-size:17px;font-weight:700;margin-bottom:6px}
.welcome p{font-size:8px;line-height:10.4px}
.welcome .more{display:inline-block;margin-top:5px;font-size:7px;background:rgba(255,255,255,.3);border:1px solid #fff;padding:1px 6px}
.dots{left:323px;top:385px;display:flex;gap:6px}
.dots i{width:8px;height:8px;border-radius:50%;border:2px solid var(--brand);background:#fff}
.dots i:first-child{background:var(--brand)}
.service{top:423px;width:112px}
.service .pic{height:70px;border:1px solid var(--line);border-radius:3px}
.service h2{font-size:12px;color:var(--brand);font-weight:700;text-align:center;margin-top:5px;white-space:nowrap}
.service p{font-size:8.4px;line-height:10.4px;margin-top:5px;color:#333}
.btn{top:586px;width:31px;height:12px;background:#111;color:#fff;font-size:7px;text-align:center;line-height:12px;border-radius:2px}
.feature{top:618px;width:140px;text-align:center}
.feature .tab{display:inline-block;background:var(--brand);color:#fff;font-size:9px;font-weight:700;padding:2px 10px;border-radius:3px 3px 0 0}
.feature .pic{height:68px;border:2px solid var(--brand)}
.feature p{font-size:8.4px;line-height:10.4px;margin-top:5px;color:#333}
.partners{left:0;top:762px;width:682px;height:46px;background:var(--band)}
.partner{top:778px;font-size:13px;font-weight:700;color:#333}
.quote{top:830px;width:230px}
.avatar{width:46px;height:46px;border-radius:50%;border:2px solid var(--brand);background:linear-gradient(#eaf1f8,#8a98a8)}
.qtext{font-size:8.4px;line-height:10.4px;color:#555;text-align:center;width:160px}
.qmark{font-family:"Open Sans",sans-serif;font-size:20px;font-weight:700;color:var(--brand);line-height:1}
.col-h{top:912px;font-family:"Open Sans",sans-serif;font-size:11px;font-weight:600;color:var(--heading)}
.blog-title{left:100px;top:931px;font-family:"Open Sans",sans-serif;font-size:10px;font-weight:600;color:var(--heading)}
.blog-meta{left:100px;top:944px;font-size:6px;font-weight:700;color:#333}
.date{left:100px;top:965px;width:31px;height:33px;text-align:center;color:#fff;font-size:9px}
.date .m{background:#222;height:17px;line-height:17px}
.date .d{background:var(--brand);height:16px;line-height:16px;font-weight:700}
.blog-ex{left:138px;top:967px;width:105px;font-size:7.6px;line-height:9px;color:#444}
.testi{left:270px;top:954px;width:140px;font-family:"Open Sans",sans-serif;font-style:italic;font-size:6px;line-height:8.8px;color:var(--brand)}
.project{left:446px;top:933px;width:136px;height:65px;background:#e2e2e2;padding:4px}
.project div{background:#fff;height:57px;display:flex;align-items:center;justify-content:center;font-size:15px;color:#111;gap:6px}
.project div i{width:10px;height:10px;border-radius:50%;background:var(--brand)}
.view{top:1016px;font-family:"Open Sans",sans-serif;font-size:6.4px;color:var(--brand);text-decoration:underline;font-weight:600}
.news{left:78px;top:1046px;width:524px;height:40px;border:1px solid #9cc3e6;border-radius:4px;background:#f1f6fb}
.news-text{left:150px;top:1056px;width:190px;font-size:7.4px;line-height:9.6px;color:#333}
.news-input{left:348px;top:1058px;width:150px;height:18px;border:1px solid #9bb;background:#fff;font-family:"Open Sans",sans-serif;font-style:italic;font-size:7px;color:#777;padding:4px 8px}
.news-btn{left:510px;top:1058px;width:82px;height:18px;background:var(--brand);color:#fff;font-size:8px;text-align:center;line-height:18px}
.footer{left:0;top:1107px;width:682px;height:77px;background:var(--footer)}
.footer-bar{left:0;top:1184px;width:682px;height:16px;background:var(--footer-bar);color:#9ab;font-size:6px;padding:4px 100px}
.f-text{font-size:8.4px;line-height:11.6px;color:#fff}
.social{top:1135px;width:23px;height:23px;border:2px solid #fff;border-radius:50%}
</style>
</head>
<body>
<div class="abs topline"></div>
<div class="abs logo">Volbex</div>
<div class="abs register">Register Your Business</div>
<div class="abs search"><span>Search...</span><b><svg width="11" height="11" viewBox="0 0 11 11"><circle cx="4.5" cy="4.5" r="3.3" fill="none" stroke="#fff" stroke-width="1.3"/><line x1="7" y1="7" x2="10" y2="10" stroke="#fff" stroke-width="1.4"/></svg></b></div>
<nav class="abs nav"><span>Home</span><i>|</i><span>About Us</span><i>|</i><span>Services</span><i>|</i><span>Advice ▾</span><i>|</i><span>Advisers Profile</span><i>|</i><span>Login</span><i>|</i><span>Sign Up</span><i>|</i><span>Help</span></nav>

<div class="abs hero" role="img" aria-label="Photo of an adviser and a client reviewing documents at a desk"></div>
<div class="abs hero-line"></div>
<div class="abs welcome">
  <h1>Welcome to Volbex</h1>
  <p>Dummy text is text that is used in the publishing industry or by web designers to occupy the space which will later be filled with 'real' content. This is required when, for example, the final text is not yet available. Dummy text is also known as 'fill text'. It is said that song composers of the past used dummy texts as lyrics when writing melodies in order to have a 'ready-made' text to sing with the melody. Dummy texts have been in use by typesetters since the 16th century.</p>
  <span class="more">More</span>
</div>
<div class="abs dots"><i></i><i></i><i></i></div>

<div class="abs service" style="left:99px"><div class="pic" role="img" aria-label="Stacked coins" style="background:linear-gradient(#fff,#d9c79a)"></div><h2>Debt funding advice</h2><p>Dummy text is also used to demonstrate the appear-ance of different typefaces and layouts, and in general the content of dummy text is nonsensical.</p></div>
<div class="abs service" style="left:223px"><div class="pic" role="img" aria-label="Judge's gavel and scales" style="background:linear-gradient(#fbf7f1,#9a6a3e)"></div><h2>Legal advice</h2><p>Dummy text is also used to demonstrate the appear-ance of different typefaces and layouts, and in general the content of dummy text is nonsensical.</p></div>
<div class="abs service" style="left:346px"><div class="pic" role="img" aria-label="Hands using a calculator over papers" style="background:linear-gradient(#dfe6ef,#4c5a6c)"></div><h2>Accountant advice</h2><p>Dummy text is also used to demonstrate the appear-ance of different typefaces and layouts, and in general the content of dummy text is nonsensical.</p></div>
<div class="abs service" style="left:470px"><div class="pic" role="img" aria-label="Tablet showing analysis charts" style="background:linear-gradient(#eaf3fb,#5b8fc4)"></div><h2>Analysis</h2><p>Dummy text is also used to demonstrate the appear-ance of different typefaces and layouts, and in general the content of dummy text is nonsensical.</p></div>
<div class="abs btn" style="left:134px">More</div>
<div class="abs btn" style="left:263px">More</div>
<div class="abs btn" style="left:386px">More</div>
<div class="abs btn" style="left:507px">More</div>

<div class="abs feature" style="left:100px"><span class="tab">Who We Are</span><div class="pic" role="img" aria-label="Hand with pen over printed charts" style="background:linear-gradient(#c9d7e6,#6d86a6)"></div><p>Its function as a filler or as a tool for comparing the visual impression of different typefaces</p></div>
<div class="abs feature" style="left:270px"><span class="tab">What We Do</span><div class="pic" role="img" aria-label="Business team meeting" style="background:linear-gradient(#ecebe6,#6e6a62)"></div><p>Its function as a filler or as a tool for comparing the visual impression of different typefaces</p></div>
<div class="abs feature" style="left:440px"><span class="tab">Why choose Us</span><div class="pic" role="img" aria-label="Person touching a digital network of contacts" style="background:linear-gradient(#3f86c9,#0c2f5a)"></div><p>Its function as a filler or as a tool for comparing the visual impression of different typefaces</p></div>

<div class="abs partners"></div>
<div class="abs partner" style="left:101px">quantiora</div>
<div class="abs partner" style="left:218px">Tessaly</div>
<div class="abs partner" style="left:300px;color:#1d3f8f">Kinetra</div>
<div class="abs partner" style="left:422px;color:#4d8a88">Harbourleaf</div>
<div class="abs partner" style="left:524px;color:#b3232e;font-size:11px;top:780px">Vitrelle</div>

<div class="abs quote" style="left:101px"><div class="abs avatar" role="img" aria-label="Portrait of a client" style="left:0;top:0"></div><span class="abs qmark" style="left:56px;top:0">“</span><p class="abs qtext" style="left:66px;top:8px">Dummy text is text that is used in the publishing industry or by web designers to occupy the space which will later be filled with 'real' content.</p><span class="abs qmark" style="left:190px;top:44px">”</span></div>
<div class="abs quote" style="left:364px"><div class="abs avatar" role="img" aria-label="Portrait of a client" style="left:0;top:0"></div><span class="abs qmark" style="left:56px;top:0">“</span><p class="abs qtext" style="left:60px;top:8px">Dummy text is text that is used in the publishing industry or by web designers to occupy the space which will later be filled with 'real' content.</p><span class="abs qmark" style="left:188px;top:44px">”</span></div>

<div class="abs col-h" style="left:102px">Recent Blog</div>
<div class="abs col-h" style="left:270px">Testimonials</div>
<div class="abs col-h" style="left:436px">Latest Project</div>
<div class="abs blog-title">The standard Lorem Ipsum</div>
<div class="abs blog-meta">Bonorum ,jan29,14 20comments</div>
<div class="abs date"><div class="m">Aug</div><div class="d">31</div></div>
<p class="abs blog-ex">"Lorem ipsum dolor sit amet, consectetur adipiscing elit, sed do eiusmod ...</p>
<div class="abs testi"><b style="font-style:normal;font-size:9px">“</b> I'm a South Jersey Realtor and have experi-enced a lot of sub-par cleaning companies. However, when I met Pat about ...<br><br>Bright Parcels/Sunday Fiesta, LLC</div>
<div class="abs project"><div><span>northvane</span><i></i></div></div>
<div class="abs view" style="left:101px">View all articles</div>
<div class="abs view" style="left:272px">View all Projects</div>
<div class="abs view" style="left:437px">View all Project</div>

<div class="abs news"></div>
<svg class="abs" style="left:110px;top:1057px" width="30" height="20" viewBox="0 0 30 20"><rect x="1" y="1" width="28" height="18" rx="2" fill="none" stroke="#0b5aa6" stroke-width="2"/><path d="M1 2 L15 12 L29 2" fill="none" stroke="#0b5aa6" stroke-width="2"/></svg>
<p class="abs news-text">Lorem Ipsum is simply dummy text of the printing and typesetting industry...</p>
<div class="abs news-input">Enter your e-mail ..</div>
<div class="abs news-btn">submit</div>

<footer class="abs footer"></footer>
<svg class="abs" style="left:99px;top:1134px" width="14" height="20" viewBox="0 0 14 20"><path d="M7 0C3 0 0 3 0 7c0 5 7 13 7 13s7-8 7-13c0-4-3-7-7-7z" fill="#fff"/><circle cx="7" cy="7" r="2.6" fill="#0a4f99"/></svg>
<p class="abs f-text" style="left:125px;top:1132px">Volbex services,<br>12-16 Quill Lane,<br>AU.</p>
<svg class="abs" style="left:260px;top:1131px" width="14" height="24" viewBox="0 0 14 24"><rect x="1" y="1" width="12" height="22" rx="2" fill="none" stroke="#fff" stroke-width="2"/><circle cx="7" cy="19" r="1.3" fill="#fff"/></svg>
<p class="abs f-text" style="left:284px;top:1126px;line-height:14px"><span style="font-size:7.4px">Phone #: +65 6100-2384</span><br>info@volbex.co.uk<br>support@volbex.co.uk</p>
<div class="abs social" role="img" aria-label="Social profile link" style="left:448px"></div>
<div class="abs social" role="img" aria-label="Social profile link" style="left:481px"></div>
<div class="abs social" role="img" aria-label="Social profile link" style="left:514px"></div>
<div class="abs social" role="img" aria-label="Peerlane profile link" style="left:547px"></div>
<div class="abs footer-bar">Copyright © 2007-2014 Volbexservices. All rights reserved.</div>
</body>
</html>
```